Professional Home Buyer business card needed

I need a pretty straight forward business card designed. We help people that NEED to sell their homes solve problems. We perform all types of Real Estate transactions including flip, wholesale, investment, rental property and multi family. The card will mainly be used to give to prospective Sellers but will also be given to Real Estate Investors as well. It should professional and very easy to read, most clients are older people.

Target Market(s)

Distressed home sellers as well as Real Estate investors

Industry/Entity Type

Real Estate

Contact Information for Business Card

should be a professional layout

Colors
ec1f27
ffffff
000000

Requirements
Must have
• Large logo on back and smaller one on front. should utilize Red, white, and black.
• I am thinking of using a soft touch coating on the card so keep that in mind.
• Contact info should be very easy to read, think older clients.
Nice to have
• I would like to see a design with rounded corners on the card
Should not have
• pictures of homes or other home graphics.

```html
<!DOCTYPE html>
<html lang="en">
<head>
<meta charset="utf-8">
<title>Summit Home Buyers – Business Card</title>
<link href="https://fonts.googleapis.com/css2?family=Roboto:wght@400;500;700;900&display=swap" rel="stylesheet">
<style>
  :root {
    --red: #ec1f27;
    --red-dark: #a3141a;
    --white: #ffffff;
    --black: #000000;
    --backdrop: #d3e5ec;
    --radius: 20px;
  }
  * { box-sizing: border-box; margin: 0; padding: 0; }
  html, body { width: 1200px; height: 900px; overflow: hidden; }
  body {
    background: var(--backdrop);
    font-family: "Roboto", Arial, sans-serif;
    position: relative;
  }
  .card {
    position: absolute;
    left: 310px;
    width: 580px;
    height: 330px;
    border-radius: var(--radius);
    overflow: hidden;
    box-shadow: 0 6px 18px rgba(0,0,0,0.18);
  }

  /* Back of card */
  .card-back { top: 70px; background: var(--black); }
  .card-back .brand {
    position: absolute; left: 0; right: 0; top: 96px;
    text-align: center;
    color: var(--white);
    font-weight: 900;
    font-size: 50px;
    line-height: 1.1;
    letter-spacing: 1px;
    text-transform: uppercase;
  }
  .card-back .brand-line { display: block; white-space: nowrap; }
  .card-back .brand-mark {
    display: inline-block; width: 22px; height: 22px;
    background: var(--red); margin-right: 14px; vertical-align: 6px;
  }
  .card-back .website {
    position: absolute; left: 0; right: 0; bottom: 44px;
    text-align: center; color: var(--white);
    font-size: 15px; letter-spacing: 0.3px;
  }

  /* Front of card */
  .card-front { top: 500px; background: var(--white); }
  .card-front .panel { position: absolute; inset: 0; }
  .card-front .brand {
    position: absolute; left: 38px; top: 74px;
    width: 200px;
    color: var(--black);
    font-weight: 900; font-size: 24px; line-height: 1.15;
    text-transform: uppercase; letter-spacing: 0.5px;
  }
  .card-front .brand-line { display: block; white-space: nowrap; }
  .card-front .brand-mark {
    display: inline-block; width: 12px; height: 12px;
    background: var(--red); margin-right: 8px; vertical-align: 3px;
  }
  .nameplate {
    position: absolute; left: 262px; top: 36px;
    width: 318px; height: 54px;
    color: var(--white); padding-left: 40px; padding-top: 7px;
  }
  .nameplate .person { font-size: 22px; font-weight: 700; display: block; }
  .nameplate .role { font-size: 12px; font-weight: 400; display: block; margin-left: 52px; margin-top: 1px; }

  .contact-list {
    position: absolute; left: 38px; bottom: 36px;
    list-style: none;
  }
  .contact-list li {
    display: flex; align-items: center;
    font-size: 16px; color: var(--black);
    margin-top: 10px; white-space: nowrap;
  }
  .contact-list li:first-child { font-size: 19px; }
  .contact-icon {
    width: 24px; height: 24px; background: var(--red);
    margin-right: 12px; flex: none;
    display: flex; align-items: center; justify-content: center;
  }
  .address {
    position: absolute; right: 34px; bottom: 52px;
    width: 190px; text-align: center;
    color: var(--white); font-size: 15px; line-height: 1.35;
  }
  .address svg { display: block; margin: 0 auto 8px; }
</style>
</head>
<body>

  <section class="card card-back" aria-label="Card back">
    <div class="brand">
      <span class="brand-line"><span class="brand-mark"></span>Summit</span>
      <span class="brand-line">Home Buyers</span>
    </div>
    <div class="website">www.prairiehomesforcash.com</div>
  </section>

  <section class="card card-front" aria-label="Card front">
    <svg class="panel" width="580" height="330" viewBox="0 0 580 330" aria-hidden="true">
      <polygon points="255,0 580,0 580,330 355,330" fill="var(--black)"/>
      <polygon points="262,36 580,36 580,90 262,90" fill="var(--red)"/>
      <polygon points="262,90 300,90 300,108" fill="var(--red-dark)"/>
    </svg>

    <div class="brand">
      <span class="brand-line"><span class="brand-mark"></span>Summit</span>
      <span class="brand-line">Home Buyers</span>
    </div>

    <div class="nameplate">
      <span class="person">Daniel Hartley</span>
      <span class="role">President</span>
    </div>

    <ul class="contact-list">
      <li>
        <span class="contact-icon">
          <svg width="14" height="14" viewBox="0 0 24 24"><path fill="#fff" d="M6.6 10.8a15 15 0 0 0 6.6 6.6l2.2-2.2c.3-.3.7-.4 1-.2 1.1.4 2.3.6 3.6.6.6 0 1 .4 1 1V20c0 .6-.4 1-1 1A17 17 0 0 1 3 4c0-.6.4-1 1-1h3.5c.6 0 1 .4 1 1 0 1.3.2 2.5.6 3.6.1.3 0 .7-.2 1z"/></svg>
        </span>316-555-0148
      </li>
      <li>
        <span class="contact-icon">
          <svg width="14" height="14" viewBox="0 0 24 24"><rect x="2" y="5" width="20" height="14" fill="none" stroke="#fff" stroke-width="2"/><path d="M2 5l10 8 10-8" fill="none" stroke="#fff" stroke-width="2"/></svg>
        </span>dan@prairiehomesforcash.com
      </li>
      <li>
        <span class="contact-icon">
          <svg width="14" height="14" viewBox="0 0 24 24"><circle cx="12" cy="12" r="9" fill="none" stroke="#fff" stroke-width="2"/><path d="M3 12h18M12 3c3 3 3 15 0 18M12 3c-3 3-3 15 0 18" fill="none" stroke="#fff" stroke-width="1.6"/></svg>
        </span>www.prairiehomesforcash.com
      </li>
    </ul>

    <div class="address">
      <svg width="14" height="18" viewBox="0 0 24 32"><path fill="#fff" d="M12 0a12 12 0 0 0-12 12c0 9 12 20 12 20s12-11 12-20A12 12 0 0 0 12 0zm0 17a5 5 0 1 1 0-10 5 5 0 0 1 0 10z"/></svg>
      P.O. Box 812<br>Meadowvale, KS 67190
    </div>
  </section>

</body>
</html>
```